New Website for Corriveld House at www.corriveld.com.au

A new logo has been designed (through pixel forum) and we now want to align the look and feel of our website at www.corriveld.com.au to the new logo. The content and page names (e.g. Grounds) will remain largely unchanged for the new site, so please submit a new look "Home" page, using our new logo, current text and any photos you choose from the existing gallery at our website. I have also attached the current "Home" page photos.

Industry/Entity Type

Accommodation

Number of Pages Required

1 page

Requirements
Must have
• Logo to be presented on white background.

```html
<!DOCTYPE html>
<html lang="en">
<head>
<meta charset="utf-8">
<title>Corriveld House – Home</title>
<link rel="stylesheet" href="https://fonts.googleapis.com/css2?family=Open+Sans:wght@400;600;700&family=Great+Vibes&display=swap">
<style>
:root{
  --blue:#1e9ad6;
  --blue-dark:#1683bb;
  --ink:#333333;
  --muted:#6b6b6b;
  --line:#d5d5d5;
  --white:#ffffff;
  --night:#1e1e1e;
  --night-2:#2a2a2a;
}
*{box-sizing:border-box;margin:0;padding:0}
html,body{width:1200px;height:4972px;overflow:hidden}
body{font-family:"Open Sans",Arial,sans-serif;color:var(--ink);background:var(--white);position:relative}
.abs{position:absolute}
.script{font-family:"Great Vibes",cursive;font-weight:400}
.center{left:0;width:1200px;text-align:center}

/* hero */
.hero{top:0;left:0;width:1200px;height:653px;background:
  radial-gradient(ellipse at 30% 60%,rgba(255,170,80,.45),transparent 45%),
  radial-gradient(ellipse at 75% 55%,rgba(255,190,100,.35),transparent 40%),
  linear-gradient(180deg,#5d7d95 0%,#2e4a5c 40%,#1d3240 75%,#0f1d27 100%)}
.brand-plate{top:232px;left:330px;width:540px;height:130px;background:var(--white);border-radius:6px;display:flex;align-items:center;justify-content:center}
.brand-name{font-size:56px;font-weight:600;color:var(--blue);white-space:nowrap}
.nav-bar{top:597px;left:0;width:1200px;height:56px;background:rgba(10,18,24,.55)}
.nav{top:612px;left:0;width:1200px;display:flex;justify-content:center;gap:42px;list-style:none}
.nav li{font-size:15px;color:var(--white);letter-spacing:.5px;padding-bottom:6px}
.nav li.active{border-bottom:2px solid var(--white)}
.notch{top:640px;left:540px}

/* intro */
.eyebrow{font-size:22px;color:var(--ink)}
.script-title{font-size:40px;color:var(--blue)}
.intro-text{top:850px;left:200px;width:800px;text-align:center;font-size:14px;line-height:21px;color:var(--muted)}
.feature{width:250px;text-align:center}
.feature-icon{width:106px;height:106px;border-radius:50%;background:var(--blue);margin:0 auto;display:flex;align-items:center;justify-content:center;box-shadow:0 0 0 6px #e3f2fa}
.feature h3{font-size:20px;font-weight:400;margin-top:34px}
.feature p{font-size:14px;line-height:20px;color:var(--muted);margin-top:8px}
.btn{display:inline-block;width:150px;height:40px;line-height:38px;border-radius:20px;font-size:12px;text-align:center;margin-top:30px}
.btn-fill{background:var(--blue);color:var(--white);border:1px solid var(--blue)}
.btn-line{border:1px solid var(--line);color:#9a9a9a}

/* services grid */
.services{top:1303px;left:0;width:1200px;height:540px;display:grid;grid-template-columns:repeat(3,400px);grid-template-rows:repeat(2,270px)}
.service{position:relative;padding:72px 0 0 122px;color:var(--white)}
.service .label{font-size:20px}
.service .name{font-size:34px;color:var(--blue);line-height:36px;white-space:nowrap}
.btn-ghost{display:inline-block;margin-top:22px;width:150px;height:50px;line-height:46px;border:2px solid var(--white);border-radius:25px;font-size:13px;text-align:center;color:var(--white)}
.btn-ghost.on{background:var(--blue);border-color:var(--blue)}

/* gallery */
.gallery-main{top:2092px;left:232px;width:739px;height:444px;background:
  radial-gradient(ellipse at 20% 25%,#f6b66b,transparent 45%),
  linear-gradient(180deg,#6a8fb0 0%,#c9a27a 40%,#7a5a44 70%,#3e3128 100%)}
.thumbs{top:2546px;left:232px;width:739px;display:flex;gap:10px}
.thumb{flex:1;height:110px}
.view-all{top:2776px;font-size:12px;color:var(--ink)}

/* stats */
.stats{top:2801px;left:0;width:1200px;height:255px;background:linear-gradient(180deg,#dbe6ef 0%,#b9c9d6 45%,#8a99a6 75%,#5e6a75 100%)}
.stat{width:260px;text-align:center}
.stat .num{font-size:44px;color:var(--ink);margin-top:6px}
.stat .cap{font-size:13px;color:#3d4650;letter-spacing:.5px}

/* tour */
.tour{top:3056px;left:0;width:1200px;height:176px;background:var(--night)}
.tour-title{top:3100px;left:83px;font-size:38px;color:var(--white);white-space:nowrap}
.tour-title em{font-style:normal;color:var(--blue)}
.tour-text{top:3162px;left:83px;font-size:15px;color:#bdbdbd}
.pill{height:56px;line-height:54px;border-radius:28px;font-size:13px;text-align:center;color:var(--white)}
.pill-dark{background:#3a3a3a}
.pill-line{border:2px solid var(--white)}

/* testimonials */
.quote-name{top:3475px;font-size:18px}
.quote-name small{font-size:13px;color:var(--muted)}
.quote-box{top:3507px;left:152px;width:896px;height:133px;border:1px solid var(--line);padding:22px 70px;text-align:center;font-size:14px;line-height:22px;color:var(--muted)}
.arrow-box{width:32px;height:40px;border:1px solid var(--line);background:var(--white);display:flex;align-items:center;justify-content:center}
.dots{top:3674px;left:560px;display:flex;gap:12px}
.dots span{width:10px;height:10px;border-radius:50%;background:#cfcfcf}
.dots span.on{background:var(--blue)}

/* news */
.news{top:3739px;left:0;width:1200px;height:571px;background:linear-gradient(180deg,#3b4956 0%,#4f5d69 40%,#2c3640 75%,#1c232a 100%)}
.light{color:var(--white)}
.news-card{top:3981px;width:420px;color:var(--white)}
.news-img{height:165px;background:linear-gradient(90deg,#e07a1f 0%,#6d8f3a 45%,#dba46c 70%,#6fa5c7 100%)}
.news-meta{display:flex;justify-content:space-between;align-items:baseline;margin-top:14px}
.news-meta h4{font-size:18px;font-weight:400}
.news-meta span{font-size:12px}
.news-card p{font-size:13px;line-height:19px;margin-top:6px;width:300px}

/* subscribe */
.subscribe{top:4300px;left:0;width:1200px;height:92px;background:var(--night-2)}
.subscribe-title{top:4318px;left:248px;font-size:38px;color:var(--blue);white-space:nowrap}
.subscribe-field{top:4322px;left:547px;width:400px;height:50px;border-radius:25px;background:#3d3d3d;padding-left:28px;font-size:13px;color:#9a9a9a;line-height:50px}
.subscribe-go{top:4324px;left:899px;width:46px;height:46px;border-radius:50%;background:#6d6d6d;display:flex;align-items:center;justify-content:center}

/* footer */
.footer{top:4392px;left:0;width:1200px;height:580px;background:var(--night)}
.footer-plate{top:4448px;left:420px;width:360px;height:100px;background:var(--white);border-radius:6px;display:flex;align-items:center;justify-content:center}
.footer-plate .brand-name{font-size:34px}
.contact{width:320px;text-align:center;color:var(--white)}
.contact-icon{width:66px;height:66px;border-radius:50%;background:var(--blue);margin:0 auto;display:flex;align-items:center;justify-content:center;box-shadow:0 0 0 6px rgba(30,154,214,.25)}
.contact h5{font-size:18px;font-weight:400;margin-top:22px}
.contact p{font-size:13px;line-height:20px;color:#bdbdbd}
.copyright{top:4855px;font-size:12px;color:#bdbdbd}
.copyright b{color:var(--blue);font-weight:400}
.social{top:4900px;left:543px;display:flex;gap:14px}
.social span{width:36px;height:36px;border-radius:50%;border:1px solid #8a8a8a}
</style>
</head>
<body>

<!-- Hero -->
<div class="abs hero" role="img" aria-label="Evening view of the mansion with lit windows reflected in the pool"></div>
<div class="abs brand-plate"><span class="brand-name">Corriveld House</span></div>
<div class="abs nav-bar"></div>
<ul class="abs nav">
  <li class="active">HOME</li><li>MANSION</li><li>GALLERY</li><li>LOCATION</li><li>AVAILABILITY</li><li>CONTACT</li>
</ul>
<svg class="abs notch" width="120" height="40" viewBox="0 0 120 40"><path d="M0 13 C30 13 40 40 60 40 C80 40 90 13 120 13Z" fill="#fff"/><path d="M50 20 L60 28 L70 20" stroke="#555" stroke-width="2" fill="none"/></svg>

<!-- Intro -->
<div class="abs center eyebrow" style="top:752px">We are</div>
<div class="abs center script script-title" style="top:776px">Corriveld House</div>
<p class="abs intro-text">On over 2 manicured garden acres, Corriveld House is a unique Coastvale estate, centrally located in the prestigious rural suburb of Bramwood. Magnificent properties rarely feel so warm and welcoming – so browse away and visit our photo gallery – and we look forward to having you stay as our guests.</p>

<div class="abs feature" style="top:968px;left:84px">
  <div class="feature-icon"><svg width="46" height="46" viewBox="0 0 24 24" fill="none" stroke="#fff" stroke-width="1.4"><path d="M12 21s-6-6.2-6-11a6 6 0 0 1 12 0c0 4.8-6 11-6 11z"/><circle cx="12" cy="10" r="2.2"/></svg></div>
  <h3>Many Locations</h3><p>Lorem Ipsum is simply dummy text of the printing and typesetting industry.</p>
  <span class="btn btn-fill">LEARN MORE</span>
</div>
<div class="abs feature" style="top:968px;left:342px">
  <div class="feature-icon"><svg width="46" height="46" viewBox="0 0 24 24" fill="none" stroke="#fff" stroke-width="1.4"><circle cx="12" cy="12" r="8"/><path d="M4 12h16M12 4c3 3 3 13 0 16M12 4c-3 3-3 13 0 16"/></svg></div>
  <h3>Renting Services</h3><p>Lorem Ipsum is simply dummy text of the printing and typesetting industry.</p>
  <span class="btn btn-line">LEARN MORE</span>
</div>
<div class="abs feature" style="top:968px;left:601px">
  <div class="feature-icon"><svg width="46" height="46" viewBox="0 0 24 24" fill="none" stroke="#fff" stroke-width="1.4"><circle cx="12" cy="12" r="3"/><path d="M12 3v3M12 18v3M3 12h3M18 12h3M5.6 5.6l2.1 2.1M16.3 16.3l2.1 2.1M5.6 18.4l2.1-2.1M16.3 7.7l2.1-2.1"/></svg></div>
  <h3>Property Management</h3><p>Lorem Ipsum is simply dummy text of the printing and typesetting industry.</p>
  <span class="btn btn-line">LEARN MORE</span>
</div>
<div class="abs feature" style="top:968px;left:860px">
  <div class="feature-icon"><svg width="46" height="46" viewBox="0 0 24 24" fill="none" stroke="#fff" stroke-width="1.4"><circle cx="12" cy="12" r="8"/><path d="M8 15l3-3 2 2 4-4M14 10h3v3"/></svg></div>
  <h3>Free Market Analysis</h3><p>Lorem Ipsum is simply dummy text of the printing and typesetting industry.</p>
  <span class="btn btn-line">LEARN MORE</span>
</div>

<!-- Services grid -->
<div class="abs services">
  <div class="service" role="img" aria-label="Mansion exterior photo" style="background:linear-gradient(160deg,#5b6f7c,#2f3a42)"><div class="label">We Provide you</div><div class="script name">Mansion</div><span class="btn-ghost on">VIEW DETAIL</span></div>
  <div class="service" role="img" aria-label="Bedroom interior photo" style="background:linear-gradient(160deg,#6a5a4e,#2e2823)"><div class="label">We Provide you</div><div class="script name">Bedrooms</div><span class="btn-ghost">VIEW DETAIL</span></div>
  <div class="service" role="img" aria-label="Guest house photo" style="background:linear-gradient(160deg,#5e6a5a,#2b302a)"><div class="label">We Provide you</div><div class="script name">Guest House</div><span class="btn-ghost">VIEW DETAIL</span></div>
  <div class="service" role="img" aria-label="Event terrace photo" style="background:linear-gradient(160deg,#4f5a62,#24292d)"><div class="label">We Provide you</div><div class="script name">Stay &amp; Event</div><span class="btn-ghost">VIEW DETAIL</span></div>
  <div class="service" role="img" aria-label="Garden grounds photo" style="background:linear-gradient(160deg,#4e6448,#22301f)"><div class="label">We Provide you</div><div class="script name">Grounds</div><span class="btn-ghost">VIEW DETAIL</span></div>
  <div class="service" role="img" aria-label="Wedding lawn photo" style="background:linear-gradient(160deg,#56694e,#263022)"><div class="label">We Provide you</div><div class="script name">Diy Weddings</div><span class="btn-ghost">VIEW DETAIL</span></div>
</div>

<!-- Gallery -->
<div class="abs center eyebrow" style="top:1893px;font-size:20px">Awesome Portfolio</div>
<div class="abs center script script-title" style="top:1917px">Our Beautiful Gallery</div>
<p class="abs intro-text" style="top:1985px;left:190px;width:820px">Lorem Ipsum is simply dummy text of the printing and typesetting industry. Lorem Ipsum has been the industry's standard dummy text ever since the 1500s.</p>
<svg class="abs" style="top:2040px;left:588px" width="24" height="16" viewBox="0 0 24 16"><path d="M2 2l10 8 10-8M2 8l10 8 10-8" stroke="#bbb" stroke-width="1.5" fill="none"/></svg>
<div class="abs gallery-main" role="img" aria-label="Poolside lounge at sunset with palm trees"></div>
<div class="abs thumbs">
  <div class="thumb" role="img" aria-label="Living room photo" style="background:linear-gradient(135deg,#a58b74,#5c4a3d)"></div>
  <div class="thumb" role="img" aria-label="Dining area photo" style="background:linear-gradient(135deg,#c99a5e,#6b4b2c)"></div>
  <div class="thumb" role="img" aria-label="Bedroom photo" style="background:linear-gradient(135deg,#d8cfc4,#8a7d70)"></div>
  <div class="thumb" role="img" aria-label="Patio photo" style="background:linear-gradient(135deg,#8fb3d1,#51616e)"></div>
  <div class="thumb" role="img" aria-label="Lounge photo" style="background:linear-gradient(135deg,#b98a66,#4f3a2c)"></div>
  <div class="thumb" role="img" aria-label="Kitchen photo" style="background:linear-gradient(135deg,#c4b6a4,#6a5c4e)"></div>
</div>
<svg class="abs" style="top:2715px;left:585px" width="30" height="30" viewBox="0 0 30 30"><rect x="4" y="8" width="22" height="16" rx="2" fill="none" stroke="#bbb" stroke-width="1.5"/><circle cx="15" cy="16" r="4" fill="none" stroke="#bbb" stroke-width="1.5"/></svg>
<div class="abs center view-all">VIEW ALL</div>

<!-- Stats -->
<div class="abs stats" role="img" aria-label="Snowy mountain range under a pale sky"></div>
<div class="abs stat" style="top:2848px;left:69px">
  <svg width="52" height="46" viewBox="0 0 26 23" fill="none" stroke="#1e9ad6" stroke-width="1.3"><path d="M2 11L13 2l11 9M5 9v12h16V9M10 21v-6h6v6"/></svg>
  <div class="num">975+</div><div class="cap">MENSION USED</div>
</div>
<div class="abs stat" style="top:2848px;left:334px">
  <svg width="46" height="46" viewBox="0 0 23 23" fill="none" stroke="#1e9ad6" stroke-width="1.3"><circle cx="11.5" cy="7" r="4.5"/><path d="M3 22c0-5 4-8 8.5-8s8.5 3 8.5 8"/></svg>
  <div class="num">1425+</div><div class="cap">HAPPY CLIENTS</div>
</div>
<div class="abs stat" style="top:2848px;left:599px">
  <svg width="46" height="46" viewBox="0 0 23 23" fill="none" stroke="#1e9ad6" stroke-width="1.3"><circle cx="11.5" cy="14" r="7"/><path d="M8 3h7l-3.5 4z"/></svg>
  <div class="num">400+</div><div class="cap">DIY WEDDINGS</div>
</div>
<div class="abs stat" style="top:2848px;left:858px">
  <svg width="46" height="46" viewBox="0 0 23 23" fill="none" stroke="#1e9ad6" stroke-width="1.3"><circle cx="11.5" cy="8" r="6"/><circle cx="11.5" cy="8" r="3"/><path d="M7.5 13l-2 8 6-3 6 3-2-8"/></svg>
  <div class="num">50+</div><div class="cap">AWARDE WINNER</div>
</div>

<!-- Tour -->
<div class="abs tour"></div>
<div class="abs script tour-title">Lets <em>have a tour</em> &amp; you will love it</div>
<div class="abs tour-text">Lorem Ipsum is simply dummy text of the printing and typesetting industry.</div>
<div class="abs pill pill-dark" style="top:3116px;left:756px;width:152px">VIEW MORE</div>
<div class="abs pill pill-line" style="top:3116px;left:935px;width:185px">TAKE A TOUR</div>

<!-- Testimonials -->
<div class="abs center eyebrow" style="top:3280px;font-size:20px">Our Testimonials</div>
<div class="abs center script script-title" style="top:3304px">What they says</div>
<p class="abs intro-text" style="top:3372px;left:190px;width:820px">Lorem Ipsum is simply dummy text of the printing and typesetting industry. Lorem Ipsum has been the industry's standard dummy text ever since the 1500s.</p>
<div class="abs quote-name" style="left:478px">PERRY LANE <small>&nbsp;-&nbsp; NEW ZEALAND</small></div>
<div class="abs" style="top:3505px;left:600px;width:90px;height:2px;background:var(--blue)"></div>
<div class="abs quote-box">Lorem Ipsum is simply dummy text of the printing and typesetting industry. Lorem Ipsum has been the industry's standard dummy text ever since the 1500s, when an unknown printer took a galley of type and scrambled it to make a type specimen book. It has survived not only five centuries.</div>
<div class="abs arrow-box" style="top:3553px;left:122px"><svg width="10" height="14" viewBox="0 0 10 14"><path d="M8 1L2 7l6 6" stroke="#999" stroke-width="2" fill="none"/></svg></div>
<div class="abs arrow-box" style="top:3553px;left:1046px"><svg width="10" height="14" viewBox="0 0 10 14"><path d="M2 1l6 6-6 6" stroke="#1e9ad6" stroke-width="2" fill="none"/></svg></div>
<div class="abs dots"><span class="on"></span><span></span><span></span></div>

<!-- News -->
<div class="abs news" role="img" aria-label="Dark mountain landscape at dusk"></div>
<div class="abs center eyebrow light" style="top:3794px;font-size:20px">Our News</div>
<div class="abs center script script-title" style="top:3818px">Latest Posts</div>
<p class="abs intro-text" style="top:3874px;left:190px;width:820px;color:#fff">Lorem Ipsum is simply dummy text of the printing and typesetting industry. Lorem Ipsum has been the industry's standard dummy text ever since the 1500s.</p>
<svg class="abs" style="top:3935px;left:588px" width="24" height="16" viewBox="0 0 24 16"><path d="M2 2l10 8 10-8M2 8l10 8 10-8" stroke="#ddd" stroke-width="1.5" fill="none"/></svg>
<div class="abs news-card" style="left:166px">
  <div class="news-img" role="img" aria-label="Child playing outdoors"></div>
  <div class="news-meta"><h4>News Title</h4><span>Date : 15 Jan 2016</span></div>
  <p>Lorem Ipsum is simply dummy text of the printing and typesetting industry.</p>
</div>
<div class="abs news-card" style="left:623px">
  <div class="news-img" role="img" aria-label="Child playing outdoors"></div>
  <div class="news-meta"><h4>News Title</h4><span>Date : 15 Jan 2016</span></div>
  <p>Lorem Ipsum is simply dummy text of the printing and typesetting industry.</p>
</div>

<!-- Subscribe -->
<div class="abs subscribe"></div>
<div class="abs script subscribe-title">Subscribe Here :</div>
<div class="abs subscribe-field">E-Mail Address</div>
<div class="abs subscribe-go"><svg width="18" height="14" viewBox="0 0 18 14"><path d="M1 7h15M11 2l5 5-5 5" stroke="#fff" stroke-width="2" fill="none"/></svg></div>

<!-- Footer -->
<div class="abs footer"></div>
<div class="abs footer-plate"><span class="brand-name">Corriveld House</span></div>
<div class="abs" style="top:4654px;left:298px;width:600px;height:1px;background:#444"></div>
<div class="abs contact" style="top:4621px;left:138px">
  <div class="contact-icon"><svg width="28" height="28" viewBox="0 0 24 24" fill="none" stroke="#fff" stroke-width="1.6"><path d="M12 21s-6-6.2-6-11a6 6 0 0 1 12 0c0 4.8-6 11-6 11z"/><circle cx="12" cy="10" r="2.2"/></svg></div>
  <h5>ADDRESS</h5><p>18 Corriveld Drive Bramwood, Coastvale<br>Queensland, Australia</p>
</div>
<div class="abs contact" style="top:4621px;left:440px">
  <div class="contact-icon"><svg width="28" height="28" viewBox="0 0 24 24" fill="none" stroke="#fff" stroke-width="1.6"><rect x="4" y="9" width="16" height="9" rx="1"/><path d="M7 9V4h10v5M7 15h10v5H7z"/></svg></div>
  <h5>FAX</h5><p>1300 482 916</p>
</div>
<div class="abs contact" style="top:4621px;left:738px">
  <div class="contact-icon"><svg width="28" height="28" viewBox="0 0 24 24" fill="none" stroke="#fff" stroke-width="1.6"><circle cx="12" cy="12" r="8"/><path d="M4 12h16M12 4c3 3 3 13 0 16M12 4c-3 3-3 13 0 16"/></svg></div>
  <h5>WEBSITE</h5><p>WWW.CORRIVELD.COM.AU</p>
</div>
<div class="abs center copyright">© <b>CORRIVELD HOUSE</b> - 2016, All Rights Reserved.</div>
<div class="abs social"><span></span><span></span><span></span></div>

</body>
</html>
```